Commercial Business Card - stand out, clean, simple, unique.

commercial real estate group located in Texas. Called 4 Pines Real Estate. We want a unique yet clean and professional card. On one side I would like the 4P to be by itself or to look as unique or tasteful as possible. We have the logo in white, black, and color in case a black background or something similar looks best on one side. We need a space for our name, email, cell. website. And possibly room for a phrase or city.

Contact Information for Business Card

Name, Title, Email, Phone Number, website

```html
<!DOCTYPE html>
<html lang="en">
<head>
<meta charset="utf-8">
<title>4 Pines Real Estate – Business Card</title>
<link href="https://fonts.googleapis.com/css2?family=Cinzel:wght@500;600&family=Lato:wght@400;700&display=swap" rel="stylesheet">
<style>
  :root {
    --stage: #2b2b2b;
    --card: #050507;
    --card-edge: #0d0f16;
    --brand-blue: #2f4fb0;
    --band-blue: #1f46a6;
    --accent-orange: #e88a3a;
    --accent-red: #c23a2a;
    --ghost: rgba(40, 60, 120, 0.18);
    --text-light: #f2f2f2;
  }
  * { box-sizing: border-box; margin: 0; padding: 0; }
  html, body { width: 1200px; height: 930px; overflow: hidden; }
  body {
    background: var(--stage);
    font-family: "Lato", Arial, sans-serif;
    position: relative;
  }
  .card {
    position: absolute;
    width: 600px;
    height: 343px;
    background: radial-gradient(ellipse at 45% 40%, var(--card-edge), var(--card) 70%);
    overflow: hidden;
    box-shadow: 0 14px 30px rgba(0,0,0,0.55);
  }
  .card--front { left: 130px; top: 85px; }
  .card--back  { left: 470px; top: 500px; }

  .ghost-mark {
    position: absolute;
    border-radius: 50%;
    background: var(--ghost);
  }
  .card--front .ghost-mark { width: 250px; height: 250px; left: 200px; top: 40px; }
  .card--back .ghost-mark  { width: 260px; height: 260px; left: 300px; top: -40px; }

  .brand {
    position: absolute;
    display: flex;
    align-items: center;
    gap: 12px;
  }
  .brand__square {
    width: 30px; height: 30px;
    background: var(--brand-blue);
  }
  .brand__name {
    font-family: "Cinzel", Georgia, serif;
    font-weight: 600;
    color: var(--brand-blue);
    font-size: 26px;
    letter-spacing: 1px;
    white-space: nowrap;
  }
  .card--front .brand { left: 50%; top: 50%; transform: translate(-50%, -50%); }
  .card--back .brand { left: 38px; top: 48px; }
  .card--back .brand__name { font-size: 21px; }
  .card--back .brand__square { width: 24px; height: 24px; }

  .holder {
    position: absolute;
    right: 38px; top: 110px;
    text-align: right;
  }
  .holder__name {
    font-family: "Cinzel", Georgia, serif;
    font-weight: 600;
    color: var(--brand-blue);
    font-size: 27px;
    letter-spacing: 0.5px;
  }
  .holder__title {
    color: var(--text-light);
    font-size: 14px;
    margin-top: 2px;
  }
  .divider {
    position: absolute;
    left: 38px; right: 38px; top: 178px;
    height: 1.5px;
    background: var(--accent-orange);
  }
  .contact {
    position: absolute;
    left: 38px; top: 196px;
    list-style: none;
    color: var(--text-light);
    font-size: 14px;
    line-height: 22px;
  }
  .contact li { display: flex; align-items: center; gap: 9px; }
  .contact svg { width: 11px; height: 11px; fill: var(--brand-blue); flex: none; }
  .address {
    position: absolute;
    right: 38px; top: 200px;
    text-align: right;
    color: var(--text-light);
    font-size: 14px;
    line-height: 20px;
  }
  .bands { position: absolute; left: 0; bottom: 0; width: 600px; height: 60px; }
</style>
</head>
<body>

  <section class="card card--front" aria-label="Card front">
    <div class="ghost-mark" aria-hidden="true"></div>
    <div class="brand">
      <span class="brand__square" aria-hidden="true"></span>
      <span class="brand__name">4 Pines Real Estate</span>
    </div>
  </section>

  <section class="card card--back" aria-label="Card back">
    <div class="ghost-mark" aria-hidden="true"></div>
    <div class="brand">
      <span class="brand__square" aria-hidden="true"></span>
      <span class="brand__name">4 Pines Real Estate</span>
    </div>

    <div class="holder">
      <div class="holder__name">DANIEL HARPER</div>
      <div class="holder__title">Director</div>
    </div>

    <div class="divider"></div>

    <ul class="contact">
      <li>
        <svg viewBox="0 0 24 24" aria-hidden="true"><path d="M6.6 10.8a15 15 0 006.6 6.6l2.2-2.2c.3-.3.7-.4 1-.2 1.1.4 2.3.6 3.6.6.6 0 1 .4 1 1V20c0 .6-.4 1-1 1C10.6 21 3 13.4 3 4c0-.6.4-1 1-1h3.5c.6 0 1 .4 1 1 0 1.3.2 2.5.6 3.6.1.3 0 .7-.2 1z"/></svg>
        (512) 630-4185
      </li>
      <li>
        <svg viewBox="0 0 24 24" aria-hidden="true"><path d="M2 5h20v14H2zm2 2v.5l8 5 8-5V7zm0 2.8V17h16V9.8l-8 5z"/></svg>
        info@4pinesrealestate.com
      </li>
      <li>
        <svg viewBox="0 0 24 24" aria-hidden="true"><circle cx="12" cy="12" r="10"/></svg>
        www.4pinesrealestate.com
      </li>
    </ul>

    <div class="address">
      1840 Cedar Hollow Lane<br>
      Austin, TX 78704
    </div>

    <svg class="bands" viewBox="0 0 600 60" preserveAspectRatio="none" aria-hidden="true">
      <defs>
        <linearGradient id="warmBand" x1="0" x2="1" y1="0" y2="0">
          <stop offset="0" stop-color="#c23a2a"/>
          <stop offset="1" stop-color="#e88a3a"/>
        </linearGradient>
      </defs>
      <rect x="0" y="48" width="400" height="12" fill="url(#warmBand)"/>
      <polygon points="412,20 600,20 600,60 404,60" fill="#1f46a6"/>
    </svg>
  </section>

</body>
</html>
```